Velmar Industrial Coatings

We are looking to improve our business cards. Our company installs industrial floor and wall coatings in industrial, chemical and food processing plants.
Our coatings which consist of epoxy, urethane, and vinyl esters provide chemical and abrasion resistant surface with non-skid properties that are easy to clean.

Target Market(s)

food manufacturing, chemical plants, breweries and wineries, warehouses, clean room floors.

Industry/Entity Type

Construction

Contact Information for Business Card

improved current logo.

Colors

Designer to choose colors to be used in the design.

Requirements
Must have
• the information from uploaded file
Nice to have
• "We'll be outstanding on your floors."

```html
<!DOCTYPE html>
<html lang="en">
<head>
<meta charset="utf-8">
<title>Velmar Industrial Coatings – Business Card</title>
<link rel="stylesheet" href="https://fonts.googleapis.com/css2?family=Arimo:wght@400;700&display=swap">
<style>
  :root {
    --brand-green: #0f9e3e;
    --card-black: #171717;
    --card-white: #ffffff;
    --ink: #111111;
    --wash: #f1f1f1;
    --page: #ffffff;
  }
  * { box-sizing: border-box; margin: 0; padding: 0; }
  html, body {
    width: 955px; height: 1200px; overflow: hidden;
    background: var(--page);
    font-family: "Arimo", Arial, sans-serif;
  }
  .sheet { position: relative; width: 955px; height: 1200px; }
  .card {
    position: absolute; top: 469px;
    width: 420px; height: 262px;
    overflow: hidden;
    box-shadow: 4px 10px 16px rgba(0,0,0,0.28);
  }
  .card--front { left: 43px; background: var(--card-black); }
  .card--back { left: 491px; background: var(--card-white); }

  .wordmark {
    position: absolute; left: 0; width: 418px; top: 108px;
    text-align: center;
    color: var(--card-white);
    font-weight: 700; font-size: 50px; letter-spacing: 0.5px;
    line-height: 1;
  }
  .wordmark-sub {
    position: absolute; right: 130px; top: 163px;
    color: var(--card-white);
    font-weight: 700; font-size: 12px; letter-spacing: 0.3px;
  }

  .background-wash {
    position: absolute; right: 0; top: 0; width: 300px; height: 262px;
    background: linear-gradient(200deg, var(--wash) 0%, rgba(241,241,241,0) 70%);
  }
  .side-band {
    position: absolute; left: 0; top: 0; width: 46px; height: 262px;
    background: var(--brand-green);
  }
  .side-band-text {
    position: absolute; left: 23px; top: 131px;
    transform: translate(-50%, -50%) rotate(-90deg);
    white-space: nowrap;
    color: var(--card-white);
    font-weight: 700; font-size: 11px;
  }
  .name {
    position: absolute; left: 75px; top: 48px;
    font-weight: 700; font-size: 24px; color: var(--ink); letter-spacing: 0.5px;
  }
  .toll-free {
    position: absolute; right: 51px; top: 58px;
    font-weight: 700; font-size: 11px; color: var(--ink);
  }
  .address {
    position: absolute; left: 46px; right: 0; top: 120px; text-align: center;
    padding-left: 8px;
    font-weight: 700; font-size: 11.5px; color: var(--ink);
  }
  .contact-list {
    position: absolute; left: 119px; top: 155px; width: 221px;
    list-style: none;
  }
  .contact-list li {
    display: flex; justify-content: space-between;
    font-weight: 700; font-size: 9.5px; line-height: 13.5px;
  }
  .contact-label { color: var(--brand-green); }
  .contact-value { color: var(--ink); }
  .website {
    position: absolute; left: 46px; right: 0; top: 244px; text-align: center;
    font-weight: 700; font-size: 8px; color: var(--brand-green);
  }
</style>
</head>
<body>
<main class="sheet">

  <section class="card card--front" aria-label="Business card front">
    <div class="wordmark">Velmar</div>
    <div class="wordmark-sub">Industrial Coatings</div>
  </section>

  <section class="card card--back" aria-label="Business card back">
    <div class="background-wash" role="img" aria-label="Faint light grey background pattern"></div>
    <div class="side-band"><span class="side-band-text">Velmar Industrial Coatings inc.</span></div>
    <h1 class="name">RAY CALDER</h1>
    <p class="toll-free">1-800-555-0142</p>
    <p class="address">Velmar Inc, PO Box 42 Ridgefield, WA 98642</p>
    <ul class="contact-list">
      <li><span class="contact-label">Cell</span><span class="contact-value">(360) 555-0117</span></li>
      <li><span class="contact-label">Office</span><span class="contact-value">(360) 555-0128</span></li>
      <li><span class="contact-label">Fax</span><span class="contact-value">(360) 555-0139</span></li>
      <li><span class="contact-label">Email</span><span class="contact-value">ray@velmarfloors.com</span></li>
    </ul>
    <p class="website">www.velmarfloors.com</p>
  </section>

</main>
</body>
</html>
```